SEHLAN REAL ESTATE
شركة السهلان العقارية
Creative Brief
Simple
FAISAL ALQUDRANI
Real Estate Consultant & Developer
SAUDI ARABIA.JEDDAH
f_alqudrani@mailvesta.com
THE LOGO
Yasahiro17 Yasahiro17
YADESIGN YADESIGN

```html
<!DOCTYPE html>
<html lang="en">
<head>
<meta charset="utf-8">
<title>Sehlan Real Estate – Business Cards</title>
<link href="https://fonts.googleapis.com/css2?family=Cinzel:wght@400;500&family=Noto+Naskh+Arabic:wght@500&family=Lato:wght@400&display=swap" rel="stylesheet">
<style>
  :root {
    --page-bg: #ffffff;
    --card-white: #ffffff;
    --brand-blue: #2e7fc2;
    --ink-blue: #2f6ea6;
    --ink-grey: #6c7784;
    --shadow: rgba(0,0,0,0.16);
  }
  html, body {
    margin: 0; padding: 0;
    width: 1200px; height: 871px;
    overflow: hidden;
    background: var(--page-bg);
  }
  .canvas { position: relative; width: 1200px; height: 871px; }
  .card {
    position: absolute; top: 343px;
    width: 406px; height: 293px;
    box-shadow: 0 2px 6px var(--shadow);
  }
  .card--front { left: 186px; background: var(--card-white); }
  .card--back  { left: 620px; background: var(--brand-blue); }

  .brand { position: absolute; left: 0; right: 0; text-align: center; }
  .brand__name {
    font-family: "Cinzel", serif; font-weight: 500;
    letter-spacing: 1px; margin: 0; line-height: 1;
    display: inline-flex; align-items: center; gap: 8px;
  }
  .brand__dot { display: inline-block; border-radius: 50%; }
  .brand__arabic {
    font-family: "Noto Naskh Arabic", serif; font-weight: 500;
    margin: 4px 0 0; line-height: 1.2; direction: rtl;
  }
  .card--front .brand { top: 58px; }
  .card--front .brand__name { font-size: 19px; color: var(--ink-blue); }
  .card--front .brand__dot { width: 9px; height: 9px; background: var(--ink-blue); }
  .card--front .brand__arabic { font-size: 15px; color: var(--ink-blue); }

  .card--back .brand { top: 96px; }
  .card--back .brand__name { font-size: 30px; color: #fff; }
  .card--back .brand__dot { width: 13px; height: 13px; background: #fff; }
  .card--back .brand__arabic { font-size: 24px; color: #fff; }

  .person { position: absolute; left: 50px; top: 148px; }
  .person__name {
    font-family: "Cinzel", serif; font-size: 11px; color: var(--ink-blue);
    margin: 0; letter-spacing: .5px;
  }
  .person__role {
    font-family: "Lato", sans-serif; font-size: 5.5px; color: var(--ink-grey);
    margin: 2px 0 0; text-transform: uppercase; letter-spacing: .3px;
  }
  .contact { position: absolute; left: 218px; top: 127px; list-style: none; margin: 0; padding: 0; }
  .contact__item {
    display: flex; align-items: center; gap: 6px; height: 24px;
    font-family: "Lato", sans-serif; font-size: 6px; color: var(--ink-grey);
    text-transform: uppercase; letter-spacing: .3px;
  }
  .contact__icon { width: 9px; height: 9px; fill: var(--ink-blue); }
</style>
</head>
<body>
<main class="canvas">
  <section class="card card--front">
    <div class="brand">
      <p class="brand__name"><span class="brand__dot"></span>SEHLAN REAL ESTATE</p>
      <p class="brand__arabic">شركة السهلان العقارية</p>
    </div>
    <div class="person">
      <p class="person__name">FAISAL ALQUDRANI</p>
      <p class="person__role">Real Estate Consultant &amp; Developer</p>
    </div>
    <ul class="contact">
      <li class="contact__item">
        <svg class="contact__icon" viewBox="0 0 10 10"><path d="M5 0a3.5 3.5 0 0 0-3.5 3.5C1.5 6 5 10 5 10s3.5-4 3.5-6.5A3.5 3.5 0 0 0 5 0zm0 5a1.5 1.5 0 1 1 0-3 1.5 1.5 0 0 1 0 3z"/></svg>
        Saudi Arabia.Jeddah
      </li>
      <li class="contact__item">
        <svg class="contact__icon" viewBox="0 0 10 10"><path d="M2 .5l2 2-1 1.2a6 6 0 0 0 3.3 3.3L7.5 6l2 2-1.3 1.5C4.5 9.5.5 5.5.5 1.8z"/></svg>
        +966 50 123 4567
      </li>
      <li class="contact__item">
        <svg class="contact__icon" viewBox="0 0 10 10"><path d="M0 2h10v6H0zM.8 2.6 5 5.6l4.2-3v.9L5 6.5.8 3.5z"/></svg>
        f_alqudrani@mailvesta.com
      </li>
    </ul>
  </section>

  <section class="card card--back">
    <div class="brand">
      <p class="brand__name"><span class="brand__dot"></span>SEHLAN REAL ESTATE</p>
      <p class="brand__arabic">شركة السهلان العقارية</p>
    </div>
  </section>
</main>
</body>
</html>
```